Math Help Website Needs New Design

Looking to refresh the design of my existing site (brightsumguide.net) to be easier on the eyes. I am fully capable of doing the HTML coding and have for years, but I don't have the eye for good design, colors, layout, and fonts. This is where I need help!

I need both a new design scheme and a new logo that matches. The overall functionality will be the same as the existing site, and should not be unrecognizable.

Target Market(s)

It should appeal to students (age 13-22) and their parents, so it should NOT be childish in appearance, nor should it be corporate.

Requirements
Must have
• Should be simple, easy-to-navigate, and neither childish nor corporate. I am looking for a design for both the homepage and a similar "content" page. Simple, bold colors are preferred. A logo should be prominent at the top, with a search bar nearby. Below that I need a similar navigational area like I already have. Then, I need about 200px wide ad space on the left of the main body area.

```html
<!DOCTYPE html>
<html lang="en">
<head>
<meta charset="utf-8">
<title>Bright Sum Guide</title>
<link href="https://fonts.googleapis.com/css2?family=Gelasio:wght@400;500&family=Open+Sans:wght@400;600;700&display=swap" rel="stylesheet">
<style>
:root{
  --teal-dark:#1c8c97;
  --teal-light:#8fe0e4;
  --green:#2f9a45;
  --green-light:#55b866;
  --green-dark:#1f7a34;
  --purple:#3b2fb0;
  --purple-light:#5646c8;
  --ink:#222;
  --link:#2e8a3e;
  --frame:#c9c9c9;
  --orange:#f27a12;
  --muted:#6a6a6a;
}
*{box-sizing:border-box;margin:0;padding:0}
html,body{width:1200px;height:1062px;overflow:hidden;background:#fff}
body{position:relative;font-family:"Open Sans",sans-serif;color:var(--ink)}

.header{position:absolute;left:0;top:0;width:1200px;height:150px;
  background:linear-gradient(90deg,#2a9aa4 0%,#7fd6dc 35%,#4fb9c1 60%,#2d9aa3 100%)}
.header-art{position:absolute;left:470px;top:10px;width:420px;height:130px;
  background:linear-gradient(90deg,rgba(255,255,255,.05),rgba(255,255,255,.18),rgba(255,255,255,.05));border-radius:8px}
.brand{position:absolute;left:118px;top:59px;height:64px;width:258px;border-radius:50%;
  background:#fff;display:flex;align-items:center;justify-content:center;gap:8px}
.brand-dot{width:12px;height:12px;border-radius:50%;background:var(--purple)}
.brand-name{font-family:"Gelasio",serif;font-size:23px;font-weight:500;color:var(--purple);white-space:nowrap}
.search{position:absolute;left:910px;top:72px;width:180px;height:34px;border-radius:17px;
  background:#fff;border:1px solid rgba(0,0,0,.12);display:flex;align-items:center;justify-content:flex-end;padding-right:12px}

.nav{position:absolute;left:0;top:150px;width:1200px;height:44px;
  background:linear-gradient(#5cbd6b,var(--green) 55%,var(--green-dark));border-top:2px solid #8fd49a}
.nav ul{list-style:none;position:absolute;left:100px;top:0;display:flex;height:42px;align-items:center}
.nav li{font-family:"Gelasio",serif;color:#fff;font-size:17px;padding:0 20px;border-right:1px solid rgba(255,255,255,.25);white-space:nowrap}

.ad-space{position:absolute;left:94px;top:216px;width:154px;height:696px;border-radius:6px;
  background:linear-gradient(180deg,#3a3a3a 0%,#1a1a1a 62%,#f27a12 78%,#f59a3a 100%)}

.online{position:absolute;left:42px;top:930px;width:250px;text-align:center}
.online .count{color:#5aa84a;font-size:15px}
.online .sub{font-size:12px;margin-top:2px}
.live-btn{position:absolute;left:62px;top:981px;width:209px;height:35px;border-radius:5px;
  background:linear-gradient(#79c46b,#4f9e41);color:#fff;font-weight:700;font-size:16px;
  display:flex;align-items:center;justify-content:center;gap:10px;box-shadow:0 0 0 2px #d8ecd3}
.live-btn .icon{width:14px;height:16px;background:#d9f0d0;border-radius:6px 6px 3px 3px}
.study{position:absolute;left:70px;top:1036px;width:192px;text-align:center;font-size:15px;border-bottom:1px dotted #555;padding-bottom:4px}

.frame{position:absolute;border:1px solid var(--frame);background:#fff}
.hero{left:290px;top:208px;width:792px;height:234px;padding:5px}
.hero-photo{width:100%;height:100%;background:linear-gradient(90deg,#6f7f73,#8a9b90 45%,#7e9087)}
.hero h1{position:absolute;left:300px;top:30px;font-family:"Gelasio",serif;font-weight:400;
  font-size:31px;color:#fff;white-space:nowrap;text-shadow:0 1px 3px rgba(0,0,0,.4)}

.card{top:449px;width:392px;height:234px;padding:4px;background:linear-gradient(#fff 70%,#ececec)}
.card-photo{height:98px}
.card h2{font-family:"Gelasio",serif;font-weight:400;font-size:21px;text-align:center;margin:8px 0 4px}
.card p{font-size:13px;line-height:18px;padding:0 7px}
.card a{color:var(--link);text-decoration:none}

.panel{width:392px;padding-bottom:10px;background:linear-gradient(#f3f3f3,#fff 30%)}
.panel-head{height:44px;color:#fff;font-family:"Gelasio",serif;font-size:21px;display:flex;align-items:center;justify-content:center}
.panel.purple .panel-head{background:linear-gradient(var(--purple-light),var(--purple))}
.panel.green .panel-head{background:linear-gradient(var(--green-light),var(--green))}
.panel ul{list-style:none;padding:4px 22px 0 18px}
.panel li{height:36.5px;display:flex;align-items:center;gap:20px;font-family:"Gelasio",serif;font-size:14px;border-bottom:1px dotted #999;white-space:nowrap}
.panel li svg{flex:none}
.view-all{text-align:right;padding:12px 24px 0 0;font-family:"Gelasio",serif;font-size:16px;color:var(--green-dark)}
</style>
</head>
<body>
<header class="header">
  <div class="header-art" role="img" aria-label="Faint decorative math symbols and a calculator illustration"></div>
  <div class="brand"><span class="brand-dot"></span><span class="brand-name">Bright Sum Guide</span></div>
  <div class="search" role="search">
    <svg width="16" height="16" viewBox="0 0 16 16"><circle cx="6.5" cy="6.5" r="5" fill="none" stroke="#2a8c96" stroke-width="2"/><path d="M10.5 10.5L15 15" stroke="#2a8c96" stroke-width="2.4"/></svg>
  </div>
</header>
<nav class="nav">
  <ul>
    <li>Home</li><li>Algebra</li><li>Geometry</li><li>Trig</li><li>Calculus</li><li>Statistics</li><li>More Subjects +</li><li>Message Board</li>
  </ul>
</nav>

<aside class="ad-space" role="img" aria-label="Advertisement banner with black bubbles and an orange click button"></aside>

<div class="online"><div class="count">59 people online</div><div class="sub">They can help you right now!</div></div>
<div class="live-btn"><span class="icon"></span>Get Live Help</div>
<div class="study">Live Study Group</div>

<section class="frame hero">
  <div class="hero-photo" role="img" aria-label="Student writing numbers on a green chalkboard"></div>
  <h1>Welcome to Bright Sum Guide</h1>
</section>

<section class="frame card" style="left:290px">
  <div class="card-photo" role="img" aria-label="Students working at desks in a classroom" style="background:linear-gradient(90deg,#b89a80,#d8c8b8 50%,#a88c74)"></div>
  <h2>Math Lessons</h2>
  <p>Looking to understand a subject better, or maybe you don't understand what your textbook is trying to tell you? We have a collection of <a>algebra</a> and <a>geometry</a> lessons that you can view online right now.</p>
</section>
<section class="frame card" style="left:689px">
  <div class="card-photo" role="img" aria-label="People holding up question mark cards" style="background:linear-gradient(90deg,#8fa8c8,#dfe6ee 50%,#9bb2cf)"></div>
  <h2>Ask your question</h2>
  <p>on our math <a>help message board</a>. Just be sure to explain what you've tried to do and where you're stuck, and a friendly volunteer may try to assist you!</p>
</section>

<section class="frame panel purple" style="left:290px;top:691px;height:234px">
  <div class="panel-head">What's New?</div>
  <ul>
    <li><svg width="14" height="14" viewBox="0 0 14 14"><path d="M2 2L12 12M12 2L2 12" stroke="#1e1a7a" stroke-width="3"/></svg>Multiplying Polynomials</li>
    <li><svg width="14" height="14" viewBox="0 0 14 14"><path d="M2 2L12 12M12 2L2 12" stroke="#1e1a7a" stroke-width="3"/></svg>Derivative of an Inverse Function</li>
    <li><svg width="14" height="14" viewBox="0 0 14 14"><path d="M2 2L12 12M12 2L2 12" stroke="#1e1a7a" stroke-width="3"/></svg>Derivatives of Logs and Exps</li>
    <li><svg width="14" height="14" viewBox="0 0 14 14"><path d="M2 2L12 12M12 2L2 12" stroke="#1e1a7a" stroke-width="3"/></svg>Differentiating Trig Functions</li>
  </ul>
  <div class="view-all">view all</div>
</section>

<section class="frame panel purple" style="left:290px;top:933px;height:160px">
  <div class="panel-head">Math Lessons</div>
  <ul>
    <li><svg width="14" height="14" viewBox="0 0 14 14"><path d="M2 2L12 12M12 2L2 12" stroke="#1e1a7a" stroke-width="3"/></svg>Algebra</li>
    <li><svg width="14" height="14" viewBox="0 0 14 14"><path d="M2 2L12 12M12 2L2 12" stroke="#1e1a7a" stroke-width="3"/></svg>Geometry</li>
  </ul>
</section>

<section class="frame panel green" style="left:689px;top:691px;height:400px">
  <div class="panel-head">Current Discussions</div>
  <ul>
    <li><svg width="14" height="14" viewBox="0 0 14 14"><path d="M2 2L12 12M12 2L2 12" stroke="#3aa048" stroke-width="3"/></svg>Simultaneous Equation difficulty</li>
    <li><svg width="14" height="14" viewBox="0 0 14 14"><path d="M2 2L12 12M12 2L2 12" stroke="#3aa048" stroke-width="3"/></svg>Calculus - box problem</li>
    <li><svg width="14" height="14" viewBox="0 0 14 14"><path d="M2 2L12 12M12 2L2 12" stroke="#3aa048" stroke-width="3"/></svg>New 1000 challenge!</li>
    <li><svg width="14" height="14" viewBox="0 0 14 14"><path d="M2 2L12 12M12 2L2 12" stroke="#3aa048" stroke-width="3"/></svg>Can you please help me figure out thi...</li>
    <li><svg width="14" height="14" viewBox="0 0 14 14"><path d="M2 2L12 12M12 2L2 12" stroke="#3aa048" stroke-width="3"/></svg>Percents &amp; Fractional Relationships</li>
    <li><svg width="14" height="14" viewBox="0 0 14 14"><path d="M2 2L12 12M12 2L2 12" stroke="#3aa048" stroke-width="3"/></svg>counting with replacement</li>
    <li><svg width="14" height="14" viewBox="0 0 14 14"><path d="M2 2L12 12M12 2L2 12" stroke="#3aa048" stroke-width="3"/></svg>Moved - word problem - Mixture/Solution</li>
    <li><svg width="14" height="14" viewBox="0 0 14 14"><path d="M2 2L12 12M12 2L2 12" stroke="#3aa048" stroke-width="3"/></svg>Limits Homework Help</li>
    <li><svg width="14" height="14" viewBox="0 0 14 14"><path d="M2 2L12 12M12 2L2 12" stroke="#3aa048" stroke-width="3"/></svg>Volume</li>
  </ul>
</section>
</body>
</html>
```